Technical Redesign of AI-Generated Method & Topic Graphics for PowerPoint

e have a set of graphics and diagrams that were initially created using AI. The content, structure, and overall layout are already defined and should remain largely unchanged.

The objective is NOT to create completely new designs. This is primarily a technical refinement and conversion project. The graphics need to be professionally redrawn, cleaned up, and rebuilt so that they:

• Look less AI-generated and more professional/corporate
• Match our existing corporate website style
• Are fully editable in Microsoft PowerPoint
• Use consistent fonts, colors, spacing, and iconography
• Maintain the original meaning and information structure

REFERENCE WEBSITE
https://moorwald-forschung. at/

Please use the website as the primary reference for:
• Color palette
• Typography
• Visual language
• General corporate look and feel
• Professional, research-oriented appearance

The style should be clean, technical, modern, and suitable for a scientific/research institution.

SCOPE OF WORK
For each supplied graphic:

1. Recreate the graphic manually
- Do not simply trace or export the AI image.
- Rebuild all elements using PowerPoint native objects where possible.

2. Improve visual quality
- Remove typical AI-generated inconsistencies.
- Correct alignment, spacing, proportions, and visual hierarchy.
- Standardize icons and graphic elements.

3. Corporate style adaptation
- Apply colors and typography consistent with our website.
- Use a professional and technically oriented visual style.
- Avoid decorative or overly creative design elements.

4. Ensure full editability
- All text must remain editable.
- Shapes should be editable PowerPoint objects.
- Icons should preferably be vector-based.
- Elements should not be flattened into images unless absolutely necessary.

DELIVERABLES
Required output:

• Microsoft PowerPoint (.pptx)
• All graphics fully editable
• Layered and logically grouped objects
• Consistent formatting across all graphics
• Optional source files (.svg, .ai, or . eps) if available

DESIGN DIRECTION
Please focus on:

• Technical accuracy
• Professional presentation quality
• Corporate consistency
• PowerPoint usability

Please do NOT focus on:
• Creating alternative concepts
• Artistic reinterpretations
• Major layout changes
• Creative redesigns

The goal is to transform existing AI-generated diagrams into professional, corporate-standard, PowerPoint-editable graphics that fit seamlessly with the Moorwaldinstitut Graz website and presentation materials.

```html
<!DOCTYPE html>
<html lang="en">
<head>
<meta charset="utf-8">
<title>Integrated Process Assessment for Technology and Product Innovation</title>
<link rel="stylesheet" href="https://fonts.googleapis.com/css2?family=Raleway:wght@400;500;700&display=swap">
<style>
:root{
  --green:#5f7c0b;
  --green-dark:#4f6a08;
  --olive:#a4ae79;
  --charcoal:#474839;
  --stone:#a7a99b;
  --mist:#e3e5da;
  --paper:#ffffff;
  --ink:#1d1d1b;
  --card-ink:#4a4a44;
  --footer-ink:#6c6c66;
  --divider:#d8c2c2;
}
*{box-sizing:border-box;margin:0;padding:0}
html,body{width:1200px;height:733px;overflow:hidden;background:var(--paper)}
body{position:relative;font-family:"Raleway",sans-serif;color:var(--ink)}
.abs{position:absolute}
.accent-bar{left:87px;top:43px;width:87px;height:6px;background:var(--green)}
.title{left:85px;top:57px;font-size:26px;font-weight:700;letter-spacing:-.2px}
.subtitle{left:85px;top:86px;font-size:17px;font-weight:400;color:var(--green)}
.shapes{left:0;top:0;width:1200px;height:733px}
.icon-box{background:var(--paper);display:flex;align-items:center;justify-content:center}
.icon-box svg{display:block}
.block-title{color:var(--paper);font-weight:700;font-size:15.5px;line-height:18px}
.bullets{list-style:none;color:var(--paper);font-size:11.8px;line-height:14.4px}
.bullets li{position:relative;padding-left:15px}
.bullets li::before{content:"";position:absolute;left:1px;top:6px;width:3px;height:3px;border-radius:50%;background:currentColor}
.stage-title{left:462px;top:128px;color:var(--paper);font-weight:700;font-size:15px}
.stage-label{top:233px;width:110px;margin-left:-55px;text-align:center;color:var(--paper);font-size:12px}
.balance{left:86px;top:455px;width:1027px;text-align:center;color:var(--green);font-weight:700;font-size:15px}
.benefits-title{left:187px;top:512px;color:var(--paper);font-weight:700;font-size:15px}
.card{top:538px;height:39px;background:var(--paper);display:flex;align-items:center;padding:0 6px 0 7px;font-size:10.2px;line-height:13px;letter-spacing:-.1px;white-space:nowrap;color:var(--card-ink)}
.card .tick{position:absolute;right:4px;bottom:5px;width:12px;height:12px;background:var(--green);border-radius:2px}
.applicable{left:85px;top:596px;width:1030px;height:49px;background:var(--mist);display:flex;align-items:center;justify-content:center;color:var(--green);font-weight:700;font-size:18.5px}
.org{top:659px;font-size:12px;font-weight:700;color:var(--footer-ink);line-height:13px;white-space:nowrap}
.org-divider{left:198px;top:655px;width:1px;height:30px;background:var(--divider)}
.page-no{left:1085px;top:663px;width:28px;height:27px;background:var(--green);color:var(--paper);font-size:8px;display:flex;align-items:center;justify-content:center}
</style>
</head>
<body>
<div class="abs accent-bar"></div>
<h1 class="abs title">Integrated Process Assessment for Technology and Product Innovation</h1>
<p class="abs subtitle">Ecological, social and economic assessment in early development phases</p>

<svg class="abs shapes" viewBox="0 0 1200 733" aria-hidden="true">
  <polygon fill="var(--green)" points="85,117 390,117 418,193 390,270 85,270"/>
  <polygon fill="var(--green)" points="399,117 1086,117 1114,193 1086,270 399,270 426,193"/>
  <rect x="85" y="277" width="337" height="151" fill="var(--olive)"/>
  <rect x="432" y="277" width="338" height="151" fill="var(--charcoal)"/>
  <rect x="777" y="277" width="336" height="151" fill="var(--stone)"/>
  <polygon fill="var(--mist)" points="86,437 1113,437 1113,478 600,491 86,478"/>
  <rect x="85" y="499" width="1028" height="87" fill="var(--green)"/>
  <line x1="470" y1="217" x2="1042" y2="217" stroke="#d9e0c4" stroke-width="1"/>
  <g fill="var(--paper)">
    <rect x="466" y="213" width="8" height="8"/><rect x="572" y="213" width="8" height="8"/>
    <rect x="688" y="213" width="8" height="8"/><rect x="805" y="213" width="8" height="8"/>
    <rect x="921" y="213" width="8" height="8"/><rect x="1038" y="213" width="8" height="8"/>
  </g>
  <path d="M1117,193 H1136 V543 H1115" fill="none" stroke="var(--green)" stroke-width="1" stroke-dasharray="3 3"/>
  <path d="M1121,190 L1116,193 L1121,196 M1119,540 L1114,543 L1119,546" fill="none" stroke="var(--green)" stroke-width="1"/>
  <g fill="none" stroke="var(--paper)" stroke-width="2.4" stroke-linejoin="round" stroke-linecap="round">
    <path d="M460,168 h14 l6,6 v22 h-20 z M464,178 h10 M464,184 h7"/><circle cx="476" cy="191" r="4"/><path d="M479,194 l4,4"/>
    <path d="M570,186 a8,8 0 1 1 12,0 v5 h-12 z M572,196 h8 M563,174 h-3 M592,174 h-3 M566,166 l-2,-2 M586,166 l2,-2"/>
    <path d="M692,167 v-3 M682,169 h20 M685,170 l7,14 7,-14 M688,184 h8 l-4,12 z"/><circle cx="692" cy="190" r="1.5"/>
    <path d="M809,166 l14,7 v14 l-14,8 -14,-8 v-14 z M795,173 l14,7 14,-7 M809,180 v15"/>
    <path d="M937,165 c-8,1 -14,8 -17,17 l5,5 c9,-3 16,-9 17,-17 z M920,182 l-5,1 3,-7 M925,187 l-1,5 7,-3 M914,195 l5,-5"/><circle cx="932" cy="175" r="2"/>
  </g>
  <g fill="var(--paper)">
    <rect x="1028" y="190" width="4" height="8"/><rect x="1034" y="186" width="4" height="12"/>
    <rect x="1040" y="181" width="4" height="17"/><rect x="1046" y="175" width="4" height="23"/>
    <path d="M1028,183 l10,-7 5,3 9,-9" fill="none" stroke="var(--paper)" stroke-width="2.4"/>
  </g>
</svg>

<div class="abs icon-box" style="left:108px;top:125px;width:47px;height:47px">
  <svg width="28" height="30" viewBox="0 0 28 30" aria-hidden="true"><path d="M8,26 V4 M8,4 h14 l-4,5 4,5 h-14" fill="var(--green)" stroke="var(--green)" stroke-width="2.4" stroke-linejoin="round"/><circle cx="8" cy="26" r="3.5" fill="none" stroke="var(--green)" stroke-width="2"/></svg>
</div>
<h2 class="abs block-title" style="left:176px;top:130px">Starting Point &amp;<br>Methodological Foundations</h2>
<ul class="abs bullets" style="left:102px;top:183px">
  <li>Products, processes, services and systems</li>
  <li>Market, societal and sustainability requirements</li>
  <li>Goal and scope definition</li>
  <li>Reference system, data basis</li>
  <li>Scenarios and sensitivities</li>
</ul>

<h2 class="abs stage-title">Assessment along the innovation process</h2>
<span class="abs stage-label" style="left:474px">Research</span>
<span class="abs stage-label" style="left:575px">Concept</span>
<span class="abs stage-label" style="left:694px">Design</span>
<span class="abs stage-label" style="left:809px">Prototype</span>
<span class="abs stage-label" style="left:926px">Pilot</span>
<span class="abs stage-label" style="left:1041px">Market uptake</span>

<div class="abs icon-box" style="left:108px;top:285px;width:47px;height:47px">
  <svg width="32" height="30" viewBox="0 0 32 30" aria-hidden="true"><path d="M5,12 a12,12 0 0 1 21,-4 M27,18 a12,12 0 0 1 -21,4" fill="none" stroke="var(--olive)" stroke-width="2"/><rect x="9" y="10" width="7" height="14" fill="none" stroke="var(--olive)" stroke-width="1.8"/><path d="M20,24 v-8 c0,-3 3,-5 5,-5 c0,3 -2,5 -5,5" fill="none" stroke="var(--olive)" stroke-width="1.8"/><path d="M4,25 h24" stroke="var(--olive)" stroke-width="2"/></svg>
</div>
<h2 class="abs block-title" style="left:167px;top:290px">Environmental Life Cycle<br>Assessment (eLCA)</h2>
<ul class="abs bullets" style="left:102px;top:341px">
  <li>Quantification of environmental impacts and<br>benefits</li>
  <li>Comparison with a reference system</li>
  <li>Carbon footprint and broader impact categories</li>
  <li>ISO 14040/44, accredited models and databases</li>
</ul>

<div class="abs icon-box" style="left:453px;top:285px;width:47px;height:47px">
  <svg width="30" height="30" viewBox="0 0 30 30" aria-hidden="true"><g fill="var(--charcoal)"><circle cx="9" cy="6" r="3"/><circle cx="21" cy="6" r="3"/><circle cx="15" cy="8" r="3.2"/><path d="M4,16 c0,-5 10,-5 10,0 z M16,16 c0,-5 10,-5 10,0 z M9,17 c0,-5 12,-5 12,0 z"/><path d="M2,22 h7 l5,2 h8 c2,0 2,2 0,2 h-8 l-3,-1 M4,27 l5,-3 12,3 7,-5" fill="none" stroke="var(--charcoal)" stroke-width="1.8"/></g></svg>
</div>
<h2 class="abs block-title" style="left:515px;top:290px">Social Life Cycle<br>Assessment (S-LCA)</h2>
<ul class="abs bullets" style="left:450px;top:341px">
  <li>Assessment of social impacts across the life cycle</li>
  <li>Working conditions, health &amp; safety, human rights</li>
  <li>Stakeholder perspective and global value chains</li>
  <li>Social hotspot identification and relevant databases</li>
</ul>

<div class="abs icon-box" style="left:794px;top:285px;width:49px;height:47px">
  <svg width="28" height="32" viewBox="0 0 28 32" aria-hidden="true"><g fill="none" stroke="var(--stone)" stroke-width="2"><path d="M14,2 l-5,6 h3 v5 h4 v-5 h3 z" fill="var(--stone)"/><rect x="5" y="12" width="18" height="18"/><circle cx="14" cy="21" r="5"/><path d="M11,20 h5 M11,22.5 h5 M16,18 a3,3 0 1 0 0,6"/></g></svg>
</div>
<h2 class="abs block-title" style="left:859px;top:299px">Life Cycle Costing (LCC)</h2>
<ul class="abs bullets" style="left:795px;top:341px">
  <li>Economic assessment across the life cycle</li>
  <li>Cost-benefit and techno-economic evaluation</li>
  <li>Infrastructure analyses and market screening</li>
  <li>Roll-out scenarios and cost drivers</li>
</ul>

<p class="abs balance">Balancing ecology, social aspects and economy</p>

<div class="abs icon-box" style="left:94px;top:509px;width:72px;height:68px">
  <svg width="36" height="36" viewBox="0 0 36 36" aria-hidden="true"><g fill="none" stroke="var(--green)" stroke-width="2.4" stroke-linejoin="round"><path d="M20,4 h-14 v28 h12"/><rect x="9" y="9" width="4" height="4"/><rect x="9" y="16" width="4" height="4"/><rect x="9" y="23" width="4" height="4"/><circle cx="23" cy="22" r="7"/><path d="M20,22 l2,2 4,-4 M28,27 l5,5"/></g></svg>
</div>
<h2 class="abs benefits-title">Integrated Process Assessment – Concrete Benefits</h2>
<div class="abs card" style="left:185px;width:180px">Early identification of<br>opportunities and risks<span class="tick"></span></div>
<div class="abs card" style="left:371px;width:180px">Sound decision support<span class="tick"></span></div>
<div class="abs card" style="left:557px;width:180px">Comparison of technologies<br>and product options<span class="tick"></span></div>
<div class="abs card" style="left:743px;width:180px">Iterative feedback for<br>development decisions<span class="tick"></span></div>
<div class="abs card" style="left:929px;width:180px">Holistic view of ecological, social<br>and economic performance<span class="tick"></span></div>

<p class="abs applicable">Broadly applicable to diverse technologies, processes and products</p>

<span class="abs org" style="left:87px">Moorwaldinstitut<br>Graz</span>
<span class="abs org-divider"></span>
<span class="abs org" style="left:208px">Karstberg<br>Universität</span>
<span class="abs page-no">1</span>
</body>
</html>
```